Freelance Translator in Need of a Business Card

I am a freelance Japanese to English translator. I work in the video game localization industry and do literary translation in my spare time. I would like to have both the English word 'Translator' and the Japanese '翻訳者' in the job title. The final design should evoke trust, openness, and reliability.

Target Market(s)

Video game localization companies
Japanese comic book artists

Industry/Entity Type

Business

Contact Information for Business Card

Daniel Ostrowik, Translator
dan.ostrowik@quellbox.net
verolingworks.com
twitter: @verol_tx

Colors

Designer to choose colors to be used in the design.

```html
<!DOCTYPE html>
<html lang="en">
<head>
<meta charset="utf-8">
<title>Daniel Ostrowik – Translator business card</title>
<link rel="stylesheet" href="https://fonts.googleapis.com/css2?family=Open+Sans:wght@400;600&family=Noto+Sans+JP:wght@400&display=swap">
<style>
  :root {
    --page-bg: #ece8e4;
    --card-bg: #ffffff;
    --brand-blue: #1c6aa6;
    --text-grey: #4d4d4d;
    --icon-grey: #5a5a5a;
  }
  html, body {
    margin: 0;
    padding: 0;
    width: 1200px;
    height: 1000px;
    overflow: hidden;
    background: var(--page-bg);
    font-family: "Open Sans", "Noto Sans JP", sans-serif;
  }
  .canvas {
    position: relative;
    width: 1200px;
    height: 1000px;
  }
  .card {
    position: absolute;
    left: 266px;
    width: 666px;
    height: 397px;
    background: var(--card-bg);
    border-radius: 28px;
    box-shadow: 0 2px 6px rgba(0, 0, 0, 0.12);
  }
  .card--front { top: 74px; }
  .card--back { top: 533px; }

  .brand-mark {
    position: absolute;
    left: 84px;
    top: 114px;
    width: 200px;
    height: 168px;
    display: flex;
    align-items: center;
    justify-content: center;
    gap: 10px;
  }
  .brand-mark__square {
    width: 16px;
    height: 16px;
    background: var(--brand-blue);
    flex: none;
  }
  .brand-mark__name {
    font-weight: 600;
    font-size: 22px;
    color: var(--brand-blue);
    white-space: nowrap;
  }

  .divider {
    position: absolute;
    left: 330px;
    top: 122px;
    width: 2px;
    height: 154px;
    background: var(--brand-blue);
  }

  .identity {
    position: absolute;
    left: 374px;
    top: 116px;
  }
  .identity__name {
    margin: 0;
    font-weight: 600;
    font-size: 20px;
    line-height: 26px;
    color: var(--brand-blue);
    text-transform: uppercase;
    letter-spacing: 0.1px;
  }
  .identity__title {
    margin: 0;
    font-size: 15.5px;
    line-height: 22px;
    color: var(--text-grey);
  }

  .contacts {
    position: absolute;
    left: 374px;
    top: 200px;
    margin: 0;
    padding: 0;
    list-style: none;
  }
  .contacts__item {
    display: flex;
    align-items: center;
    gap: 6px;
    height: 24px;
    font-size: 16px;
    color: var(--text-grey);
  }
  .contacts__item--handle { margin-bottom: 5px; }
  .contacts__icon {
    width: 14px;
    height: 14px;
    flex: none;
  }
</style>
</head>
<body>
<main class="canvas">
  <section class="card card--front">
    <div class="brand-mark">
      <span class="brand-mark__square"></span>
      <span class="brand-mark__name">Veroling Works</span>
    </div>
    <div class="divider"></div>
    <div class="identity">
      <h1 class="identity__name">Daniel Ostrowik</h1>
      <p class="identity__title">Translator / 翻訳者</p>
    </div>
    <ul class="contacts">
      <li class="contacts__item contacts__item--handle">
        <svg class="contacts__icon" viewBox="0 0 14 14"><circle cx="7" cy="7" r="6" fill="var(--brand-blue)"/></svg>
        @verol_tx
      </li>
      <li class="contacts__item">
        <svg class="contacts__icon" viewBox="0 0 14 14"><rect x="1" y="3" width="12" height="9" fill="var(--brand-blue)"/><path d="M1.5 3.5 L7 8 L12.5 3.5" fill="none" stroke="#fff" stroke-width="1.2"/></svg>
        dan.ostrowik@quellbox.net
      </li>
      <li class="contacts__item">
        <svg class="contacts__icon" viewBox="0 0 14 14"><circle cx="7" cy="7" r="5.5" fill="none" stroke="var(--brand-blue)" stroke-width="1.5"/><path d="M1.5 7 H12.5 M7 1.5 C4 4 4 10 7 12.5 M7 1.5 C10 4 10 10 7 12.5" fill="none" stroke="var(--brand-blue)" stroke-width="1"/></svg>
        verolingworks.com
      </li>
    </ul>
  </section>

  <section class="card card--back">
    <div class="brand-mark">
      <span class="brand-mark__square"></span>
      <span class="brand-mark__name">Veroling Works</span>
    </div>
    <div class="divider"></div>
    <div class="identity">
      <h2 class="identity__name">Daniel Ostrowik</h2>
      <p class="identity__title">Translator / 翻訳者</p>
    </div>
    <ul class="contacts">
      <li class="contacts__item contacts__item--handle">
        <svg class="contacts__icon" viewBox="0 0 14 14"><circle cx="7" cy="7" r="6" fill="var(--brand-blue)"/></svg>
        @verol_tx
      </li>
      <li class="contacts__item">
        <svg class="contacts__icon" viewBox="0 0 14 14"><rect x="1" y="3" width="12" height="9" fill="var(--brand-blue)"/><path d="M1.5 3.5 L7 8 L12.5 3.5" fill="none" stroke="#fff" stroke-width="1.2"/></svg>
        dan.ostrowik@quellbox.net
      </li>
      <li class="contacts__item">
        <svg class="contacts__icon" viewBox="0 0 14 14"><circle cx="7" cy="7" r="5.5" fill="none" stroke="var(--brand-blue)" stroke-width="1.5"/><path d="M1.5 7 H12.5 M7 1.5 C4 4 4 10 7 12.5 M7 1.5 C10 4 10 10 7 12.5" fill="none" stroke="var(--brand-blue)" stroke-width="1"/></svg>
        verolingworks.com
      </li>
    </ul>
  </section>
</main>
</body>
</html>
```